Fruit Juice packaging for Canada Market

We need label designs for our Fruit juice in PET form and we have 6 flavours ( tamarind, Blueberry, Passion Fruit+ Mango, Cucumis Melo+green tea, Mulberry, and Mango.
We need designs for packaging for all 6 listed fruits

1) Blueberry Juice labeling.
2) Tamarind Juice labeling.
3) Mulberry Juice labeling.
4) Passion fruit + Mango Juice labeling.
5) Cucumis Melo+green tea Juice labeling.
6) Mango Juice labeling.

A: PET bottle shape and dimensions:
- Dimensions: please refer to attachment name: PEVRA Bottle shape
- Bottle shape: Please refer to attachment name: BOTTLE SHAPE for the actual look of the bottle design.

B: Design Ideal: we want to have a look of fresh and juicy of real fruits since we are producing RAW juices. You can chose any taken photo of fruits on Snapvault. (http://www.snapvault-example.com/photos/blueberry?phrase=Blueberry&excludenudity=true&sort=best)

C: Fonts will be up to the designer choose, easy to read, neat and easy recognize

D: Label content needs to have followings: please refer to attachment PEVRA SAMPLE DESIGN for all needed information.
Main licence Company: HALDEN Trading Inc.
Product Name: PEVRA
Product Name1 : Pevra Blueberry Juice (attached)
Flavor Name 1 : Blueberry
and
Product Name 2 : Pevra Tamarind Juice (attached)
Flavor Name 2: Tamarind
...and so on for the rest of juices

I want the design in English with editable Ai or PTS so that I can add shortly Vietnamese translation text as mandatory law in our current market-Vietnam. We will take care the translation for you.

Old labels are attached to give you an idea. Contents in the old will be pasted in your labels (nutrition facts, net weight, ingredient, direction of use... etc). you re-design to make it fresher and healthier.

On the label for 330ml PET bottle, (please see picture of sample bottle), decal dimension of L:17.5cm x H:12cm following phrase must be included:

- Made of Real Fruit Juice

- Direction of use: will be provided in Ai.
- Ingredients: will be provided in Ai.

- Production and Packaging under licence of
BORENT INC., CANADA
412 Tavernay Ouest, Quebec, CANADA.

- Importing, Producing and Distributing by RUDMOS Ltd.,
- Km7, Binh Duong city, Ho Chi Minh, Viet Nam.
- Made in Vietnam

- Nutrition Fact ( Canada label requirements)
- HALAL logo ( will be provided, show at front and on the back)
- ISO 22000:2005 logo (will be provided )
-Manufacturing date/Used by date: on the cap.
-Keep refrigerated for an even better taste.

(Somewhere in Front)

0% Cholesterol
Blueberry imports from CANADA. (for Blueberry Juice)
Delicious Tamarind from VIETNAM. ( for Tamarind juice)
Has HALAL logo at front ( see provided picture for reference)
picture of juice, fresh, wet fruits around the bottom bottle.
running juice from the juice at the bottom to the cap.

(P/S: the label packaging must meet the standard requirement for Canada)
Please request me for more info if needed.

VIETNAM and NORTH AMERICA

Pet

Serif
Sans Serif
Decorative
Script
Other font styles liked:
• Prefer to designers to chose on their design to make it looks match

Designer to choose colors to be used in the design.

• meet Canada Labeling requirement for imported products.
• Ai editable version is a must to allow us to add Vietnamese translation and movable objects on the packaging design after we add Vietnamese text.
• have done any packaging with Canadian customers with Nutrition Facts on.

```html
<!DOCTYPE html>
<html lang="en">
<head>
<meta charset="utf-8">
<title>PEVRA Juice Labels</title>
<link rel="stylesheet" href="https://fonts.googleapis.com/css2?family=Montserrat:wght@600;700&family=Marcellus&family=Arimo:wght@400;700&display=swap">
<style>
  :root {
    --page: #ffffff;
    --label: #ffffff;
    --label-edge: #e6e6e2;
    --ink: #2b2b2b;
    --mulberry: #c0201f;
    --mulberry-accent: rgba(214, 108, 84, 0.85);
    --mulberry-line: #9a2a2a;
    --blueberry: #3a2d86;
    --blueberry-accent: rgba(140, 122, 190, 0.85);
    --blueberry-line: #3d3192;
    --badge: #2f5d3a;
    --white: #ffffff;
  }
  * { box-sizing: border-box; margin: 0; padding: 0; }
  html, body { width: 1116px; height: 1200px; overflow: hidden; background: var(--page); }
  .canvas {
    position: relative; width: 1116px; height: 1200px;
    display: flex; justify-content: center; align-items: center; gap: 60px;
  }
  .label {
    position: relative; width: 340px; height: 660px;
    background: var(--label);
    border: 1px solid var(--label-edge);
    overflow: hidden;
  }
  .brand {
    position: absolute; top: 110px; left: 0; width: 100%;
    text-align: center;
    font-family: "Montserrat", sans-serif; font-weight: 700;
    font-size: 46px; letter-spacing: 3px; color: var(--ink);
  }
  .flavour-disc {
    position: absolute; left: 30px; top: 208px;
    width: 270px; height: 270px; border-radius: 50%;
  }
  .flavour-accent {
    position: absolute; left: 214px; top: 206px;
    width: 94px; height: 94px; border-radius: 50%;
  }
  .flavour-name {
    position: absolute; top: 262px; left: 0; width: 100%;
    text-align: center; color: var(--white);
    font-family: "Marcellus", serif; font-size: 37px; letter-spacing: 1px;
  }
  .flavour-kind {
    position: absolute; top: 308px; left: 0; width: 100%;
    text-align: center; color: var(--white);
    font-family: "Montserrat", sans-serif; font-weight: 600;
    font-size: 15px; letter-spacing: 2px;
  }
  .fruit-photo {
    position: absolute; left: 48px; top: 352px;
    width: 250px; height: 170px;
    border-radius: 48% 52% 45% 55% / 55% 50% 50% 45%;
  }
  .certificate {
    position: absolute; left: 30px; top: 342px;
    width: 50px; height: 50px; border-radius: 50%;
    background: var(--badge); border: 3px solid var(--white);
    box-shadow: 0 0 0 1px var(--badge);
  }
  .tagline {
    position: absolute; top: 566px; left: 0; width: 100%;
    text-align: center;
    font-family: "Marcellus", serif; font-size: 20px; letter-spacing: 1px;
  }
  .net-volume {
    position: absolute; top: 618px; left: 50%; transform: translateX(-50%);
    padding: 3px 9px; border: 1px solid var(--ink); border-radius: 12px;
    font-family: "Arimo", sans-serif; font-size: 12px; color: var(--ink);
    white-space: nowrap;
  }
  .net-volume strong { font-weight: 700; }

  .label--mulberry .flavour-disc { background: var(--mulberry); }
  .label--mulberry .flavour-accent { background: var(--mulberry-accent); }
  .label--mulberry .tagline { color: var(--mulberry-line); }
  .label--mulberry .fruit-photo {
    background: radial-gradient(ellipse at 55% 55%, #3a1c2a 0%, #5a2236 45%, #8e2236 75%, #b93a44 100%);
  }
  .label--blueberry .flavour-disc { background: var(--blueberry); }
  .label--blueberry .flavour-accent { background: var(--blueberry-accent); }
  .label--blueberry .tagline { color: var(--blueberry-line); }
  .label--blueberry .fruit-photo {
    background: radial-gradient(ellipse at 55% 50%, #4f6fa6 0%, #5b7fb8 45%, #41608f 75%, #5c8c45 100%);
  }
</style>
</head>
<body>
<main class="canvas">
  <section class="label label--mulberry">
    <div class="brand">PEVRA</div>
    <div class="flavour-disc"></div>
    <div class="flavour-accent"></div>
    <div class="flavour-name">MULBERY</div>
    <div class="flavour-kind">JUICE</div>
    <div class="fruit-photo" role="img" aria-label="Photo of fresh ripe mulberries with a green leaf"></div>
    <div class="certificate" aria-hidden="true"></div>
    <div class="tagline">pure taste, pressed fresh</div>
    <div class="net-volume">Net. Vol.: <strong>330 ml.</strong></div>
  </section>

  <section class="label label--blueberry">
    <div class="brand">PEVRA</div>
    <div class="flavour-disc"></div>
    <div class="flavour-accent"></div>
    <div class="flavour-name">BLUEBERRY</div>
    <div class="flavour-kind">JUICE</div>
    <div class="fruit-photo" role="img" aria-label="Photo of a cluster of fresh blueberries with green leaves"></div>
    <div class="certificate" aria-hidden="true"></div>
    <div class="tagline">pure taste, pressed fresh</div>
    <div class="net-volume">Net. Vol.: <strong>330 ml.</strong></div>
  </section>
</main>
</body>
</html>
```